Quilting Template Retail Label

These are laser cut acrylic templates used to trace shapes onto fabrics. Quilters use these to make repeatable cuts quickly and accurately. Sometimes referred to as quilt rulers. I need to make a label design for my line of products that shows the quality and elegance of these templates. It needs to be an eye catching design as there is stiff competition for the attention of shoppers. Feminine colors are also preferred.

The reference design will be for an item called a "Wanderers Lane 7" & 3.5" Set". The label should also say "4 piece set". The brand name is Every Piece Polymer. The Wanderers Lane is essentially a Square with a quarter of a circle cut out of it. I would like a dashed line border offset from the edge of the label, that represents the seam allowance. The seam allowance is engraved on all templates.

Pictures of the items are attached, as well as pictures of labels that I would like you to use for inspiration. The picture of the quilt is one of the designs that can be made with the Wanderers Lane template. Lastly, there are pictures of the pegboards in shops where these will be displayed, this should give you an idea of the competition.

Target Market(s)

Quilters, older women, affluent

Industry/Entity Type

Retail

Colors
e34297
e667a6
b868aa
d2a4cc

Requirements
Must have
• Must be elegant and give the feeling of a quality product.

```html
<!DOCTYPE html>
<html lang="en">
<head>
<meta charset="utf-8">
<title>Wanderers Lane 7" &amp; 3.5" Set — Every Piece Polymer</title>
<link rel="stylesheet" href="https://fonts.googleapis.com/css2?family=Great+Vibes&family=Share+Tech+Mono&display=swap">
<style>
  :root {
    --backdrop: #404040;
    --label-rose: #e34297;
    --label-pink-light: #e667a6;
    --ink-white: #ffffff;
    --ink-yellow: #f2e650;
  }
  html, body {
    margin: 0;
    padding: 0;
    width: 1200px;
    height: 1200px;
    overflow: hidden;
    background: var(--backdrop);
  }
  .canvas {
    position: relative;
    width: 1200px;
    height: 1200px;
  }
  .label {
    position: absolute;
    left: 142px;
    top: 257px;
    width: 915px;
    height: 686px;
    background: var(--label-rose);
    overflow: hidden;
  }
  .label-art {
    position: absolute;
    inset: 0;
    width: 915px;
    height: 686px;
  }
  .pattern-band { fill: var(--label-pink-light); }
  .band-rule { fill: var(--ink-white); }
  .inner-frame { fill: none; stroke: var(--ink-white); stroke-width: 2; }
  .seam-badge {
    fill: var(--label-rose);
    stroke: var(--ink-white);
    stroke-width: 5;
    stroke-dasharray: 14 9;
    stroke-linecap: butt;
  }
  .product-name {
    font-family: "Great Vibes", cursive;
    font-size: 92px;
    fill: var(--ink-white);
  }
  .piece-count {
    font-family: "Share Tech Mono", monospace;
    font-size: 62px;
    fill: var(--ink-yellow);
    letter-spacing: 2px;
  }
  .brand-name {
    font-family: "Share Tech Mono", monospace;
    font-size: 40px;
    fill: var(--ink-white);
    letter-spacing: 7px;
  }
</style>
</head>
<body>
  <main class="canvas">
    <section class="label" aria-label="Wanderers Lane 7 and 3.5 inch template set label">
      <svg class="label-art" viewBox="0 0 915 686" xmlns="http://www.w3.org/2000/svg">
        <rect class="pattern-band" x="0" y="0" width="915" height="302" role="img" aria-label="Polka dot pattern in soft pink tones"/>
        <rect class="band-rule" x="0" y="302" width="915" height="7"/>

        <polyline class="inner-frame" points="153,660 27,660 27,24 890,24 890,660 762,660"/>

        <path class="seam-badge" d="M 228 190
          C 250 160, 285 158, 310 170
          C 360 135, 420 150, 458 150
          C 496 150, 556 135, 606 170
          C 631 158, 666 160, 688 190
          C 720 195, 730 230, 722 255
          C 745 290, 735 330, 718 350
          C 735 380, 745 420, 722 445
          C 730 475, 715 510, 688 505
          C 666 530, 631 532, 606 520
          C 556 540, 496 520, 458 520
          C 420 520, 360 540, 310 520
          C 285 532, 250 530, 228 505
          C 200 510, 186 475, 194 445
          C 171 420, 181 380, 198 350
          C 181 330, 171 290, 194 255
          C 186 230, 196 195, 228 190 Z"/>

        <text class="product-name" x="458" y="283" text-anchor="middle">Wanderers</text>
        <text class="product-name" x="458" y="372" text-anchor="middle">Lane 7" &amp; 3.5"</text>
        <text class="piece-count" x="458" y="462" text-anchor="middle">4 PIECE SET</text>

        <text class="brand-name" x="458" y="673" text-anchor="middle">EVERY PIECE POLYMER</text>
      </svg>
    </section>
  </main>
</body>
</html>
```